Flyer-Design für Rücken-Massage, Klangtherapie etc.
Sehr kompetent und schnelle Umsetzung, gute Gestaltung, Farblich in Harmonie. Schnelle Änderungen, bin sehr zufrieden. Danke für die super Arbeit.
Zielgruppe
Rücken-Massage, Klangtherapie, Fußreflex-Massage, Quantenheilung
Aufgabenstellung
Text zu den Rubriken können vom Internet entnommen werden.
https://wohlruhe-tonpraxis.ch/

```html
<!DOCTYPE html>
<html lang="de">
<head>
<meta charset="utf-8">
<title>Wohlruhe-Tonpraxis – Flyer</title>
<link href="https://fonts.googleapis.com/css2?family=Oxygen:wght@300;400;700&display=swap" rel="stylesheet">
<style>
  :root{
    --bg:#d4d5d9;
    --paper:#ffffff;
    --green:#7cc11f;
    --green-light:#b4dc6e;
    --green-text:#62a814;
    --ink:#3c3c3c;
  }
  *{margin:0;padding:0;box-sizing:border-box}
  html,body{width:1200px;height:1200px;overflow:hidden;background:var(--bg);font-family:"Oxygen",sans-serif;color:var(--ink)}
  .sheet{position:absolute;top:218px;width:540px;height:764px;background:var(--paper);overflow:hidden}
  .sheet--front{left:40px}
  .sheet--back{left:620px}
  .abs{position:absolute}
  .brand{display:flex;align-items:center;gap:10px;color:var(--green);font-weight:400;line-height:1.1}
  .brand__dot{width:12px;height:12px;border-radius:50%;background:var(--green);flex:none}
  .brand__name{font-size:23px}
  .brand__owner{font-size:17px}
  .photo{position:absolute;border-radius:50%;border:5px solid var(--paper);box-shadow:0 0 0 1px #e4e4e4}
  .photo--massage{background:radial-gradient(circle at 55% 40%,#e9c2a6,#d8a889 60%,#f3ede8)}
  .photo--bowls{background:radial-gradient(circle at 50% 40%,#d9a54a,#8a4a2c 70%)}
  .photo--feet{background:radial-gradient(circle at 50% 45%,#efc8ad,#d9a88b 60%,#ece8e4)}
  .photo--meditation{background:radial-gradient(circle at 50% 45%,#8a8a8a,#e5e3e0 60%)}
  /* front */
  .headline{left:40px;top:380px;font-size:27px;line-height:34px;font-weight:400;color:#4a4a4a}
  .headline__accent{color:var(--green);font-size:35px;letter-spacing:9px;margin-left:12px;vertical-align:-6px}
  .intro{left:42px;top:512px;width:446px;font-size:12.9px;line-height:15.4px;color:var(--ink)}
  .intro--green{top:639px;color:var(--green-text)}
  /* back */
  .service{position:absolute;left:156px;width:345px;color:#fff}
  .service__title{font-size:21px;font-weight:400;letter-spacing:.3px;margin-bottom:8px}
  .service__text{font-size:12.4px;line-height:15.4px;width:335px}
  .contact{position:absolute;top:662px;font-size:15px;line-height:19px}
  .contact--left{right:327px;text-align:right}
  .contact--right{left:250px}
  .contact .accent{color:var(--green-text)}
  .contact .gap{margin-top:8px}
  .divider{position:absolute;left:229px;top:664px;width:1px;height:80px;background:var(--green)}
</style>
</head>
<body>

<section class="sheet sheet--front">
  <svg class="abs" style="left:0;top:0" width="540" height="764" viewBox="0 0 540 764">
    <defs>
      <linearGradient id="scene" x1="0" y1="0" x2="0" y2="1">
        <stop offset="0" stop-color="#4d7a3a"/>
        <stop offset=".45" stop-color="#6f9c58"/>
        <stop offset=".6" stop-color="#3fb3a4"/>
        <stop offset="1" stop-color="#1f9c8c"/>
      </linearGradient>
      <linearGradient id="waveFront" x1="0" y1="0" x2="1" y2="0">
        <stop offset="0" stop-color="#7cc11f"/>
        <stop offset="1" stop-color="#b4dc6e"/>
      </linearGradient>
    </defs>
    <path role="img" aria-label="Foto: Wasserfall im grünen Wald mit türkisem Becken" fill="url(#scene)"
      d="M76 0H540V300C500 318 470 330 420 330C360 330 300 340 250 330C200 322 160 300 130 262C110 230 90 180 80 130C74 90 70 40 76 0Z"/>
    <path fill="url(#waveFront)" d="M0 706C90 690 170 700 260 706C350 712 450 700 540 712V764H0Z"/>
    <path fill="none" stroke="#fff" stroke-width="2" d="M0 712C120 698 260 716 360 708C440 702 500 706 540 716"/>
  </svg>

  <div class="abs" style="left:25px;top:23px;width:372px;height:67px;background:var(--paper);padding:10px 12px">
    <div class="brand">
      <span class="brand__dot"></span>
      <div><div class="brand__name">Wohlruhe-Tonpraxis</div><div class="brand__owner">Mirela Hollmannsried</div></div>
    </div>
  </div>

  <div class="photo photo--massage" role="img" aria-label="Foto: Frau bei der Rückenmassage" style="left:29px;top:139px;width:150px;height:150px"></div>
  <div class="photo photo--bowls" role="img" aria-label="Foto: Klangschalen mit Klöppel und Orchidee" style="left:180px;top:247px;width:142px;height:142px"></div>
  <div class="photo photo--feet" role="img" aria-label="Foto: Fussreflexmassage an beiden Fusssohlen" style="left:353px;top:244px;width:154px;height:154px"></div>

  <h1 class="abs headline">Ihre<br>Wohlfühloase<br>für<span class="headline__accent">ENTSPANNUNG</span></h1>

  <p class="abs intro">Viele Menschen leiden unter Rückenschmerzen und -verspannungen. Grund dafür ist oftmals Stress, Bewegungsmangel, langes Sitzen und schlechte Körperhaltung. Aber auch belastende Emotionen können für Verspannungen im Rücken sorgen. Eine Massage kann diese Schmerzen lindern und auch tiefe Verspannungen lockern. Zusätzlich wird durch die Berührung der positive Energiefluss angeregt, Alltagsprobleme treten in den Hintergrund und emotionale Blockaden werden gelöst.</p>
  <p class="abs intro intro--green">Durch meine Massagen und Behandlungen helfe ich Menschen, sich von alltäglichen Verspannungen und Unruhen welche auf das Gemüt drücken, zu erlösen.</p>
</section>

<section class="sheet sheet--back">
  <div class="abs" style="left:44px;top:40px">
    <div class="brand">
      <span class="brand__dot" style="width:16px;height:16px"></span>
      <div><div class="brand__name" style="font-size:30px">Wohlruhe-Tonpraxis</div><div class="brand__owner" style="font-size:24px">Mirela Hollmannsried</div></div>
    </div>
  </div>

  <svg class="abs" style="left:0;top:125px" width="540" height="530" viewBox="0 0 540 530">
    <defs>
      <linearGradient id="band" x1="0" y1="0" x2="1" y2="0">
        <stop offset="0" stop-color="#7cc11f"/>
        <stop offset=".75" stop-color="#8cc92c"/>
        <stop offset="1" stop-color="#b4dc6e"/>
      </linearGradient>
    </defs>
    <path fill="url(#band)" d="M0 10C120 0 220 18 320 16C420 14 480 6 540 22V490C450 478 380 492 290 484C190 476 90 494 0 488Z"/>
    <path fill="none" stroke="#fff" stroke-width="2" d="M0 16C140 8 260 26 380 18C450 14 500 18 540 28"/>
    <path fill="none" stroke="#fff" stroke-width="2" d="M0 482C100 488 200 472 300 478C400 484 470 474 540 484"/>
  </svg>

  <div class="photo photo--feet" role="img" aria-label="Foto: Fussreflexmassage" style="left:42px;top:167px;width:100px;height:100px"></div>
  <div class="service" style="top:177px">
    <h2 class="service__title">FUSSREFLEXMASSAGE</h2>
    <p class="service__text">Die Blockaden werden gelöst, ein Wohlbefinden wird sich wieder einstellen, so das die Harmonie und das Gleichgewicht zum fliessen vereint.</p>
  </div>

  <div class="photo photo--bowls" role="img" aria-label="Foto: Klangschalen" style="left:42px;top:278px;width:100px;height:100px"></div>
  <div class="service" style="top:289px">
    <h2 class="service__title">KLANGSCHALEN MASSAGE</h2>
    <p class="service__text">Sie fühlen sich erholt, ruhig im Geist und körperlich entspannt. Die Lebensenergie steigt und es lösen sich schon lang vorhandene Blockaden.</p>
  </div>

  <div class="photo photo--massage" role="img" aria-label="Foto: Rücken- und Nackenmassage" style="left:42px;top:390px;width:100px;height:100px"></div>
  <div class="service" style="top:400px">
    <h2 class="service__title">RÜCKEN-NACKENMASSAGE</h2>
    <p class="service__text">Durch leichten bis starken Druck werden Muskelverspan­nungen massiert, gestrichen und geknetet. Nacken-Schul­ter und Rückenverspannungen können gelöst werden.</p>
  </div>

  <div class="photo photo--meditation" role="img" aria-label="Foto: meditierende Person im Schneidersitz" style="left:42px;top:502px;width:100px;height:100px"></div>
  <div class="service" style="top:512px">
    <h2 class="service__title">QUANTENHEILUNG</h2>
    <p class="service__text">Glaubenssätze und Blockaden lösen durch Quantenhei­lung. Die Quantenheilung ist der Oberbegriff für viele Transformationen-Methoden</p>
  </div>

  <div class="contact contact--left">
    <div class="accent">PRAXIS<br>Mirela Hollmannsried</div>
    <div class="gap">Birkenmattstr.21<br>4999 Talwil</div>
  </div>
  <div class="divider"></div>
  <div class="contact contact--right">
    <div class="accent">Rufen Sie mich an unter:</div>
    <div>076 418 52 90</div>
    <div class="accent gap">Oder besuchen Sie meine Website:</div>
    <div>www.wohlruhe-tonpraxis.ch</div>
  </div>
</section>

</body>
</html>
```